Zielgruppe
Wir vertreiben auf unserer Plattform morgenglanz58.de diverse Produkte rund um das Thema Kaffee. Unsere Zielgruppe sind Kaffeeliebhaber von jung bis alt.
Aufgabenstellung
Für unsere neue Domain vindor.at benötigen wir diverse Grafiken / Banner für die verschiedenen Bereiche unseres Shops. Momentan gibt es eine Staging Site um sich einen Überblick zu verschaffen.
Auftrag hier ist ein Startseitenbanner in der Größe 3200x1240 unter Berücksichtigung der aktuellen Farben in unserem Shop, der Thematik Kaffee und mehr und dem dazugehörigen neuen bereits entworfenem Logo.
Info Testseite: http://www.vindor.at/_staging/ Login mit admin und tulp#947
Gerne kann eigenes Bildmaterial geliefert werden

```html
<!DOCTYPE html>
<html lang="de">
<head>
<meta charset="utf-8">
<title>vindor.at – Kaffee und mehr</title>
<link rel="stylesheet" href="https://fonts.googleapis.com/css2?family=Kaushan+Script&family=Poppins:wght@400;500;600;700&display=swap">
<style>
:root{
  --brand-red:#a52b28;
  --ink:#2b211c;
  --text:#1f1f1f;
  --muted:#8d8d8d;
  --line:#3a3a3a;
  --banner-light:#efefef;
  --banner-cream:#d9b98f;
  --banner-coffee:#4a2e1d;
  --white:#ffffff;
}
*{box-sizing:border-box;margin:0;padding:0}
html,body{width:1200px;height:645px;overflow:hidden;background:var(--white);font-family:"Poppins",sans-serif;color:var(--text)}
.promo-bar{height:22px;background:var(--brand-red);color:var(--white);font-size:8.5px;display:flex;align-items:center;justify-content:center;letter-spacing:.2px}
.header{position:relative;height:146px}
.search{position:absolute;left:100px;top:43px;width:218px;height:20px;border:1px solid var(--line);border-radius:10px;display:flex;align-items:center;padding:0 6px;font-size:8.5px;color:var(--muted)}
.search span{flex:1}
.search svg{width:12px;height:12px}
.brand{position:absolute;left:50%;top:6px;transform:translateX(-50%);display:flex;flex-direction:column;align-items:center;gap:18px}
.brand-mark{width:40px;height:40px;border-radius:50%;background:var(--ink)}
.brand-name{font-weight:700;font-size:22px;color:var(--ink);line-height:1}
.tools{position:absolute;right:112px;top:44px;display:flex;align-items:center;gap:11px}
.tools svg{width:18px;height:18px;fill:none;stroke:var(--text);stroke-width:1.6}
.cart{position:relative}
.cart-badge{position:absolute;top:-6px;right:-6px;width:12px;height:12px;border-radius:50%;background:var(--brand-red);color:var(--white);font-size:7px;display:flex;align-items:center;justify-content:center}
.cart-total{font-size:10px;margin-left:-2px}
.cart-total sup{font-size:6px}
.nav{position:absolute;top:114px;left:0;right:0;display:flex;justify-content:center;gap:18px;font-size:11px;font-weight:500;letter-spacing:.1px}
.hero{position:absolute;left:99px;top:168px;width:1012px;height:392px;overflow:hidden;background:var(--banner-light)}
.hero-art{position:absolute;left:520px;top:0;right:0;bottom:0;background:radial-gradient(circle at 35% 45%,var(--banner-coffee) 0 16%,transparent 17%),radial-gradient(circle at 55% 80%,var(--banner-cream) 0 20%,transparent 21%),radial-gradient(circle at 80% 80%,#c89a68 0 18%,transparent 19%),linear-gradient(90deg,var(--banner-light) 0%,#e6ddd2 100%)}
.hero-title{position:absolute;left:24px;top:40px;font-family:"Kaushan Script",cursive;font-size:170px;line-height:1;color:var(--ink)}
.hero-sub{position:absolute;left:42px;top:214px;font-family:"Kaushan Script",cursive;font-size:86px;line-height:1;color:var(--brand-red)}
.hero-badge{position:absolute;left:862px;top:242px;width:135px;height:135px;background:var(--white);display:flex;flex-direction:column;align-items:center;justify-content:center;gap:14px}
.hero-badge .brand-mark{width:40px;height:40px}
.hero-badge .brand-name{font-size:22px}
.partners{position:absolute;left:99px;top:585px;width:1001px;height:38px;display:flex;align-items:center}
.arrow{width:19px;height:38px;border:1px solid var(--line);border-left:none;display:flex;align-items:center;justify-content:center}
.arrow.prev{border-left:1px solid var(--line);border-right:none}
.arrow svg{width:8px;height:14px;fill:none;stroke:var(--text);stroke-width:1.2}
.partner-list{flex:1;display:flex;justify-content:space-around;align-items:center}
.partner{font-size:17px;font-weight:600;color:var(--muted)}
</style>
</head>
<body>
<div class="promo-bar">Frische Garantie - Beste Markenqualität - Lieferung in 1-3 Werktagen</div>
<header class="header">
  <div class="search"><span>Suchbegriff eingeben...</span>
    <svg viewBox="0 0 24 24" fill="none" stroke="#1f1f1f" stroke-width="2.4"><circle cx="10" cy="10" r="7"/><path d="M15 15l7 7"/></svg>
  </div>
  <div class="brand"><div class="brand-mark"></div><div class="brand-name">vindor.at</div></div>
  <div class="tools">
    <svg viewBox="0 0 24 24"><path d="M12 21s-8-5-8-11a4.5 4.5 0 0 1 8-3 4.5 4.5 0 0 1 8 3c0 6-8 11-8 11z"/></svg>
    <svg viewBox="0 0 24 24"><circle cx="12" cy="8" r="4"/><path d="M4 21c1-5 15-5 16 0"/></svg>
    <div class="cart"><svg viewBox="0 0 24 24"><path d="M4 8h16v13H4z"/><path d="M8 8V6a4 4 0 0 1 8 0v2"/></svg><span class="cart-badge">0</span></div>
    <span class="cart-total">0,<sup>00*</sup></span>
  </div>
  <nav class="nav">
    <span>KAFFEE &amp; ESPRESSO</span><span>PURE TEE - TELVANO</span><span>KAFFEEKAPSELN</span><span>KAFFEEPADS</span><span>BÜRO KAFFEE SERVICE</span><span>PROBIERPAKETE</span><span>ANGEBOTE &amp; NEU</span>
  </nav>
</header>
<section class="hero">
  <div class="hero-art" role="img" aria-label="Draufsicht auf Kaffeetassen mit Espresso, Cappuccino und Latte Art"></div>
  <div class="hero-title">Kaffee</div>
  <div class="hero-sub">...und mehr</div>
  <div class="hero-badge"><div class="brand-mark"></div><div class="brand-name">vindor.at</div></div>
</section>
<div class="partners">
  <div class="arrow prev"><svg viewBox="0 0 8 14"><path d="M7 1L1 7l6 6"/></svg></div>
  <div class="partner-list">
    <span class="partner">Valdessa</span><span class="partner">Morenita</span><span class="partner">Castellan</span><span class="partner">Ferrano</span><span class="partner">Pontello</span><span class="partner">Lurazzi</span>
  </div>
  <div class="arrow next"><svg viewBox="0 0 8 14"><path d="M1 1l6 6-6 6"/></svg></div>
</div>
</body>
</html>
```